Varnek Group Business Card

Varnek Group — Business Card Design Brief
Overview
Design a double-sided business card for Varnek Group that highlights our two service arms: Varnek Communications (telecommunications) and Varnek Energy (business energy solutions). The card should feel smart and stand out when handed to clients.

Objectives
Showcase our areas of specialty clearly.
Reflect the overall Varnek / Varnek Group brand while acknowledging both arms.
Explore using both logos (Communications + Energy) or one unified logo, depending on the design.

Deliverables
One double-sided business card design (front + back).

Content & Copy
Front (preferred): Logo: Varnek / Varnek Group
Descriptor: Business Communications | Business Energy
Back:My contact details and company details
Core products: Business Mobile • Telephony • Internet • Business Energy Solutions

Brand & Visual Direction
We have a group logo currently tailored more toward telecoms, plus a separate Varnek Energy logo.
Please explore layouts that use both logos or just one, whichever works best.
Color: I wouldn't mind seeing an option using our the Blue/Purple gradient from our website (varnek-example.co.uk), but also open to non-gradient approaches and other colours..

Overall look: Smart, modern, and distinctive.
Format & Print Specs
Double-sided business card format. (Use a standard size

Must-Haves
Front: Varnek wording or Varnek Group wording with atleast 1 logo also on front “Business Communications | Business Energy.”

Back: Contact + company details and core products.
A design that stands out while remaining professional.

Nice-to-Have Options
A gradient version using our site’s Blue/Purple gradient.
A non-gradient version.
A dual-logo treatment versus a single-logo treatment.

Thanks
Dominic

```html
<!DOCTYPE html>
<html lang="en">
<head>
<meta charset="utf-8">
<title>Varnek Group Business Card</title>
<link rel="stylesheet" href="https://fonts.googleapis.com/css2?family=Poppins:wght@400;500;700&display=swap">
<style>
  :root {
    --backdrop: #3a3b3d;
    --card: #ffffff;
    --card-shade: #ededed;
    --navy: #1f1c5c;
    --text: #2c2c3a;
    --divider: #2aa3d8;
    --green-start: #3a9f3c;
    --green-end: #c6d92a;
    --blue-start: #2e58a8;
    --blue-end: #12abe0;
  }
  * { box-sizing: border-box; margin: 0; padding: 0; }
  html, body { width: 1200px; height: 900px; overflow: hidden; }
  body {
    background: var(--backdrop);
    font-family: "Poppins", sans-serif;
    position: relative;
  }
  .card {
    position: absolute;
    left: 320px;
    width: 560px;
    height: 320px;
    border-radius: 26px;
    overflow: hidden;
    background: linear-gradient(120deg, var(--card-shade), var(--card) 60%);
    box-shadow: 0 10px 24px rgba(0,0,0,.45);
  }
  .card--front { top: 80px; }
  .card--back { top: 490px; }
  .card__bands { position: absolute; inset: 0; }

  .wordmark {
    position: absolute;
    display: flex;
    align-items: center;
    gap: 10px;
    font-weight: 700;
    color: var(--navy);
    letter-spacing: 1px;
    line-height: 1;
  }
  .wordmark__dot { border-radius: 50%; flex: none; }
  .card--front .wordmark { left: 34px; top: 100px; font-size: 34px; }
  .card--front .wordmark__dot { width: 28px; height: 28px; background: var(--green-start); }
  .card--back .wordmark { left: 50%; top: 100px; transform: translateX(-50%); font-size: 50px; }
  .card--back .wordmark__dot { width: 38px; height: 38px; background: var(--blue-start); }

  .descriptor {
    position: absolute;
    left: 0; right: 0; top: 166px;
    text-align: center;
    font-size: 13px;
    font-weight: 500;
    color: var(--navy);
    letter-spacing: .4px;
  }

  .divider {
    position: absolute;
    left: 262px; top: 58px;
    width: 1px; height: 120px;
    background: var(--divider);
  }
  .contact { position: absolute; left: 282px; top: 52px; color: var(--text); }
  .contact__name { font-weight: 700; color: var(--navy); font-size: 15px; letter-spacing: .3px; }
  .contact__role { font-size: 12px; margin-bottom: 10px; }
  .contact__list { list-style: none; }
  .contact__item { display: flex; align-items: center; gap: 8px; font-size: 12px; line-height: 21px; }
  .contact__item svg { width: 13px; height: 13px; flex: none; }

  .products {
    position: absolute;
    left: 0; right: 0; top: 274px;
    text-align: center;
    font-size: 11.5px;
    font-weight: 500;
    color: var(--navy);
    letter-spacing: .3px;
  }

  .band-text {
    position: absolute;
    color: #fff;
    font-weight: 500;
    white-space: nowrap;
  }
  .card--front .band-text { left: 70px; top: 230px; font-size: 12.5px; letter-spacing: .4px; }
  .card--back .band-text { left: 90px; top: 229px; font-size: 13px; letter-spacing: 7px; }
</style>
</head>
<body>

<section class="card card--front" aria-label="Card front">
  <svg class="card__bands" viewBox="0 0 560 320" aria-hidden="true">
    <defs>
      <linearGradient id="greenBand" x1="0" x2="1">
        <stop offset="0" stop-color="var(--green-start)"/>
        <stop offset="1" stop-color="var(--green-end)"/>
      </linearGradient>
    </defs>
    <rect x="0" y="222" width="480" height="34" fill="url(#greenBand)"/>
    <rect x="470" y="196" width="90" height="24" fill="var(--green-end)"/>
    <circle cx="478" cy="216" r="26" fill="#fff"/>
    <circle cx="478" cy="216" r="20" fill="none" stroke="var(--green-start)" stroke-width="4"/>
  </svg>

  <div class="wordmark"><span class="wordmark__dot"></span>VARNEK</div>
  <div class="divider"></div>

  <div class="contact">
    <p class="contact__name">MARCUS HALE</p>
    <p class="contact__role">Director</p>
    <ul class="contact__list">
      <li class="contact__item">
        <svg viewBox="0 0 14 14"><rect x="3.5" y="1" width="7" height="12" rx="1.2" fill="none" stroke="var(--green-start)" stroke-width="1.2"/></svg>
        +44 7700 900 418
      </li>
      <li class="contact__item">
        <svg viewBox="0 0 14 14"><path d="M3 1.5l2.3 2.4-1.2 1.6a7 7 0 0 0 4.4 4.4l1.6-1.2 2.4 2.3-1.4 1.5C6.6 12.3 1.7 7.4 1.5 3z" fill="var(--green-start)"/></svg>
        +44 0113 496 0275
      </li>
      <li class="contact__item">
        <svg viewBox="0 0 14 14"><rect x="1" y="3" width="12" height="8.5" fill="var(--green-start)"/><path d="M1 3l6 5 6-5" fill="none" stroke="#fff" stroke-width="1"/></svg>
        info@varnek-example.co.uk
      </li>
      <li class="contact__item">
        <svg viewBox="0 0 14 14"><g fill="none" stroke="var(--green-start)" stroke-width="1"><circle cx="7" cy="7" r="5.8"/><ellipse cx="7" cy="7" rx="2.6" ry="5.8"/><path d="M1.2 7h11.6M2 4h10M2 10h10"/></g></svg>
        www.varnek-example.co.uk
      </li>
    </ul>
  </div>

  <p class="band-text">24 Harlow Lane, Leeds, England, LS1 7QT</p>
  <p class="products">Business Mobile • Telephony • Internet • Business Energy Solutions</p>
</section>

<section class="card card--back" aria-label="Card back">
  <svg class="card__bands" viewBox="0 0 560 320" aria-hidden="true">
    <defs>
      <linearGradient id="blueBand" x1="0" x2="1">
        <stop offset="0" stop-color="var(--blue-start)"/>
        <stop offset="1" stop-color="var(--blue-end)"/>
      </linearGradient>
    </defs>
    <rect x="0" y="222" width="480" height="34" fill="url(#blueBand)"/>
    <rect x="470" y="196" width="90" height="24" fill="var(--blue-end)"/>
    <circle cx="478" cy="216" r="26" fill="#fff"/>
    <circle cx="478" cy="216" r="20" fill="none" stroke="var(--blue-start)" stroke-width="4"/>
  </svg>

  <div class="wordmark"><span class="wordmark__dot"></span>VARNEK</div>
  <p class="descriptor">Business Communications | Business Energy</p>

  <p class="band-text">www.varnek-example.co.uk</p>
</section>

</body>
</html>
```